Interior Design & consultancy firm requires a new business card design that is a little bit funky bu

Kestrova Design Services is a leading strategic design practice specialising in the development and implementation of strategies and design solutions for commercial workplaces across a wide variety of industries.

The company has over twenty years experience in the strategic design, development and construction of innovative and efficient workplace environments for the commercial, corporate and industrial sectors.

We believe good design and efficient workspaces can transform companies, improve people’s lives and increase productivity.

Target Market(s)

My clients are mainly Government or corporate clients wanting to create a statement with their office fitout & new furniture that reflects their corporate identity

Industry/Entity Type

Construction

Font styles to use
Sans Serif

Colors
add136

Requirements
Must have
• The business card must be easy to read, simple & highlight my name & mobile phone number
Should not have
• I do not want the card to be fussy, feature too many colours or look to busy.

```html
<!DOCTYPE html>
<html lang="en">
<head>
<meta charset="utf-8">
<title>Kestrova Design Services – Business Card</title>
<link rel="stylesheet" href="https://fonts.googleapis.com/css2?family=Josefin+Sans:wght@400;600&display=swap">
<style>
  :root {
    --backdrop: #d8f07e;
    --lime: #add136;
    --charcoal-dark: #4a4a4c;
    --charcoal-light: #7a7a7c;
    --ink: #222222;
    --paper: #ffffff;
    --shadow: rgba(60, 70, 20, 0.28);
  }
  * { box-sizing: border-box; margin: 0; padding: 0; }
  html, body {
    width: 1200px; height: 900px; overflow: hidden;
    background: var(--backdrop);
    font-family: "Josefin Sans", sans-serif;
  }
  .canvas {
    position: relative; width: 1200px; height: 900px;
    display: flex; align-items: center; justify-content: center; gap: 44px;
  }
  .card {
    position: relative; width: 510px; height: 292px;
    border-radius: 3px; overflow: hidden;
    box-shadow: 0 10px 26px var(--shadow);
  }

  /* Front */
  .card--front {
    background: linear-gradient(135deg, var(--charcoal-light) 0%, var(--charcoal-dark) 55%, #3e3e40 100%);
  }
  .front__brand {
    position: absolute; left: 48px; top: 70px;
    display: flex; align-items: center; gap: 18px;
  }
  .brand-dot {
    width: 46px; height: 46px; border-radius: 50%; background: var(--lime);
  }
  .front__name {
    font-size: 64px; font-weight: 400; color: var(--lime); line-height: 1;
  }
  .front__tagline {
    position: absolute; left: 50px; top: 162px;
    font-size: 33px; font-weight: 400; color: var(--ink); letter-spacing: 0.5px;
  }
  .front__band {
    position: absolute; left: 0; right: 0; top: 226px; height: 20px;
    background: var(--lime);
  }

  /* Back */
  .card--back { background: var(--paper); }
  .back__logo {
    position: absolute; left: 34px; top: 108px;
  }
  .back__logo-name {
    font-size: 30px; font-weight: 400; color: var(--lime); line-height: 1;
  }
  .back__logo-sub {
    margin-top: 8px; font-size: 13px; color: var(--ink); letter-spacing: 0.3px;
  }
  .back__divider {
    position: absolute; left: 222px; top: 0; bottom: 0; width: 2px;
    background: var(--lime);
  }
  .back__contact {
    position: absolute; left: 248px; top: 78px; right: 20px;
  }
  .contact__name {
    font-size: 24px; font-weight: 600; color: var(--lime); letter-spacing: 1px;
    text-transform: uppercase;
  }
  .contact__role {
    margin-top: 8px; font-size: 11.5px; color: var(--ink); letter-spacing: 0.3px;
  }
  .contact__role .sep { color: var(--lime); padding: 0 3px; }
  .contact__phone {
    margin-top: 18px; font-size: 30px; font-weight: 400; color: var(--ink); letter-spacing: 1px;
  }
  .contact__rule {
    margin-top: 22px; width: 120px; height: 2px; background: var(--lime);
  }
</style>
</head>
<body>
<main class="canvas">
  <section class="card card--front" aria-label="Business card front">
    <div class="front__brand">
      <span class="brand-dot" aria-hidden="true"></span>
      <span class="front__name">Kestrova</span>
    </div>
    <p class="front__tagline">Design Services Pty. Ltd.</p>
    <div class="front__band" aria-hidden="true"></div>
  </section>

  <section class="card card--back" aria-label="Business card back">
    <div class="back__logo">
      <p class="back__logo-name">Kestrova</p>
      <p class="back__logo-sub">Design Services Pty. Ltd.</p>
    </div>
    <div class="back__divider" aria-hidden="true"></div>
    <div class="back__contact">
      <h1 class="contact__name">Marla Penfold</h1>
      <p class="contact__role">Director<span class="sep">|</span>The Senior Interior Designer</p>
      <p class="contact__phone">0412 507 283</p>
      <div class="contact__rule" aria-hidden="true"></div>
    </div>
  </section>
</main>
</body>
</html>
```